KL MOTORS BANNER/SIGN DESIGN

Design a banner sign for outdoor use for KL MOTORS - a premium pre owned vehicle sales center. The size must be 36 feet in width
and 3 feet in height.

Information required: logo (attached)
-PREMIUM PRE-OWEND VEHICLE SALES
- 517.264.3081

perhaps in smaller font: BUY-SELL-TRADE

prefer white background but could possibly do red matching the logo

```html
<!DOCTYPE html>
<html lang="en">
<head>
<meta charset="utf-8">
<title>KL Motors Banner Options</title>
<link rel="stylesheet" href="https://fonts.googleapis.com/css2?family=Archivo+Black&family=Oswald:wght@700&family=Roboto+Condensed:wght@700&family=Archivo:wght@800&display=swap">
<style>
  :root {
    --brand-red: #e0262b;
    --ink: #111111;
    --paper: #ffffff;
    --backdrop: #000000;
  }
  * { margin: 0; padding: 0; box-sizing: border-box; }
  html, body { width: 1200px; height: 1000px; overflow: hidden; background: var(--backdrop); }
  .board { position: relative; width: 1200px; height: 1000px; }
  .option-label {
    position: absolute; left: 50px;
    font-family: "Archivo Black", sans-serif; font-size: 52px; line-height: 1;
    color: var(--paper);
  }
  .banner {
    position: absolute; left: 50px; width: 1100px; height: 92px;
    background: var(--paper); overflow: hidden;
  }
  .banner-shape { position: absolute; inset: 0; }
  .brand { position: absolute; left: 18px; top: 26px; height: 40px; display: flex; align-items: center; gap: 10px; }
  .brand-dot { width: 40px; height: 40px; border-radius: 50%; border: 4px solid var(--brand-red); }
  .brand-name {
    font-family: "Archivo Black", sans-serif; font-size: 22px; letter-spacing: 1px;
    color: var(--ink); line-height: 1;
  }
  .headline {
    position: absolute; left: 0; width: 1100px; text-align: center;
    font-family: "Oswald", sans-serif; font-weight: 700; font-size: 37px; line-height: 1;
    transform: scaleX(0.92);
  }
  .headline.is-red { color: var(--brand-red); }
  .headline.is-white { color: var(--paper); }
  .tagline {
    position: absolute; left: 0; width: 1100px; text-align: center;
    font-family: "Archivo", sans-serif; font-weight: 800; font-size: 14px; line-height: 1;
    letter-spacing: 6px; color: var(--ink);
  }
  .tagline .marker { color: var(--brand-red); font-size: 9px; letter-spacing: 0; margin: 0 6px 0 0; vertical-align: 2px; }
  .contact { position: absolute; left: 876px; top: 22px; height: 48px; display: flex; align-items: center; }
  .contact-icon { width: 50px; height: 50px; }
  .contact-divider { width: 2px; height: 42px; background: var(--ink); margin: 0 6px 0 8px; }
  .contact-number {
    font-family: "Roboto Condensed", sans-serif; font-weight: 700; font-size: 23px;
    color: var(--ink); letter-spacing: 0.3px;
  }
</style>
</head>
<body>
<main class="board">

  <!-- Option A -->
  <div class="option-label" style="top:133px">A.</div>
  <section class="banner" style="top:204px">
    <div class="brand"><span class="brand-dot"></span><span class="brand-name">KL MOTORS</span></div>
    <div class="headline is-red" style="top:22px">PREMIUM PRE-OWEND VEHICLE SALES</div>
    <div class="tagline" style="top:64px">BUY-SELL-TRADE</div>
    <div class="contact">
      <svg class="contact-icon" viewBox="0 0 50 50"><circle cx="25" cy="25" r="21" fill="none" stroke="var(--brand-red)" stroke-width="4"/><path d="M17 13 l5 -1 3 7 -3 3 c2 4 5 7 9 9 l3 -3 7 3 -1 5 c-12 0 -23 -11 -23 -23z" fill="none" stroke="var(--brand-red)" stroke-width="3" stroke-linejoin="round"/></svg>
      <span class="contact-divider"></span>
      <span class="contact-number">517.264.3081</span>
    </div>
  </section>

  <!-- Option B -->
  <div class="option-label" style="top:383px">B.</div>
  <section class="banner" style="top:454px">
    <svg class="banner-shape" viewBox="0 0 1100 92"><polygon points="222,0 877,0 850,66 250,66" fill="var(--brand-red)"/></svg>
    <div class="brand"><span class="brand-dot"></span><span class="brand-name">KL MOTORS</span></div>
    <div class="headline is-white" style="top:15px">PREMIUM PRE-OWEND VEHICLE SALES</div>
    <div class="tagline" style="top:72px">BUY<span class="marker">▲</span>SELL<span class="marker">▼</span>TRADE</div>
    <div class="contact">
      <svg class="contact-icon" viewBox="0 0 50 50"><circle cx="25" cy="25" r="21" fill="none" stroke="var(--brand-red)" stroke-width="4"/><path d="M17 13 l5 -1 3 7 -3 3 c2 4 5 7 9 9 l3 -3 7 3 -1 5 c-12 0 -23 -11 -23 -23z" fill="none" stroke="var(--brand-red)" stroke-width="3" stroke-linejoin="round"/></svg>
      <span class="contact-divider"></span>
      <span class="contact-number">517.264.3081</span>
    </div>
  </section>

  <!-- Option C -->
  <div class="option-label" style="top:643px">C.</div>
  <section class="banner" style="top:714px">
    <svg class="banner-shape" viewBox="0 0 1100 92"><polygon points="210,0 838,0 890,92 250,92" fill="var(--brand-red)"/></svg>
    <div class="brand"><span class="brand-dot"></span><span class="brand-name">KL MOTORS</span></div>
    <div class="headline is-white" style="top:24px">PREMIUM PRE-OWEND VEHICLE SALES</div>
    <div class="tagline" style="top:67px">BUY<span class="marker" style="color:var(--paper)">▲</span>SELL<span class="marker" style="color:var(--paper)">▼</span>TRADE</div>
    <div class="contact">
      <svg class="contact-icon" viewBox="0 0 50 50"><circle cx="25" cy="25" r="21" fill="none" stroke="var(--brand-red)" stroke-width="4"/><path d="M17 13 l5 -1 3 7 -3 3 c2 4 5 7 9 9 l3 -3 7 3 -1 5 c-12 0 -23 -11 -23 -23z" fill="none" stroke="var(--brand-red)" stroke-width="3" stroke-linejoin="round"/></svg>
      <span class="contact-divider"></span>
      <span class="contact-number">517.264.3081</span>
    </div>
  </section>

</main>
</body>
</html>
```